Web Page for marketing online agency

We are an online marketing agency that is acing the direct response model. We engage with our customers throughout different marketing techniques as research copy-writing, advertisements and content writing. We would need a website design that will have four main aspects: The Vision; stating who we are, The Mission; stating what we do, The Team And It's Values, and a Contact Form. For this design we would want a sharp, clean and smart approach, with illustrated elements or suggestive images. You can use the attached copy, the logo, the USP and the motto. Please integrate them as you see fit while keeping in mind the previous needs and copy. This website is going to be our connection with our possible partners, future colleagues and even our clients. You may submit a design for one page or integrate the 4 different aspects on separate web pages.
Target Market(s)
business partners, future employees, age range 25-60
Industry/Entity Type
Direct Marketing
Number of Pages Required
1 page
Requirements
Must have
- Menu / Header
- 4 Parts or 4 Pages including: vision, mission, team, contact
- Logo
- Motto: Direct Brilliance
- USP: We help people help themselves.
- The copy attached
Nice to have
- Representative illustrated images or elements
Should not have
- A boring design, classical design - Pagequill like

```html
<!DOCTYPE html>
<html lang="en">
<head>
<meta charset="utf-8">
<title>Kelvaro — Direct Brilliance</title>
<link href="https://fonts.googleapis.com/css2?family=Poppins:wght@300;400;500;600;700&display=swap" rel="stylesheet">
<style>
:root{
  --blue:#29a3dc;
  --blue-light:#6cc3ea;
  --ink:#1d1d1f;
  --text:#777b80;
  --grey-band:#f2f2f3;
  --teal-dark:#0f3d55;
  --teal:#185a78;
  --black:#050505;
  --white:#ffffff;
  --field:#8fcbe9;
}
*{box-sizing:border-box;margin:0;padding:0}
html,body{width:1200px;height:3982px;overflow:hidden}
body{font-family:'Poppins',sans-serif;color:var(--ink);background:var(--white);position:relative}
.abs{position:absolute}
.backdrop{position:absolute;left:0;top:0}
/* header */
.top-rule{left:0;top:0;width:1200px;height:4px;background:var(--blue)}
.site-header{left:0;top:4px;width:1200px;height:78px;background:var(--white)}
.brand{left:112px;top:20px;display:flex;align-items:center;gap:8px;font-weight:600;font-size:30px;color:var(--ink)}
.brand-dot{width:14px;height:14px;border-radius:50%;background:var(--blue)}
.main-nav{left:395px;top:24px;display:flex;gap:14px}
.main-nav a{font-size:15px;font-weight:500;color:var(--ink);text-decoration:none;padding:6px 20px;border-radius:20px}
.main-nav a.active{background:var(--blue);color:var(--white)}
.phone{left:950px;top:30px;font-size:15px;font-weight:500;display:flex;align-items:center;gap:8px}
/* hero */
.hero{left:0;top:82px;width:1200px;height:616px;background:linear-gradient(100deg,#3b3f45 0%,#2c3036 45%,#23262b 100%)}
.hero-title{left:0;top:332px;width:1200px;text-align:center;color:var(--white);font-size:44px;font-weight:300;letter-spacing:1px}
.hero-title b{color:var(--blue);font-weight:700}
.btn-ghost{left:505px;top:420px;width:190px;height:48px;border:2px solid rgba(255,255,255,.7);border-radius:24px;color:var(--white);font-size:13px;font-weight:500;display:flex;align-items:center;justify-content:center}
/* sections */
.section-title{font-size:36px;font-weight:400;color:var(--ink)}
.section-title span{color:var(--blue)}
.body-copy{font-size:13px;line-height:22px;color:var(--text)}
.btn-more{width:138px;height:36px;border:2px solid #bfc7cf;border-radius:18px;font-size:12px;color:var(--blue);font-weight:500;display:flex;align-items:center;justify-content:center;background:var(--white)}
.photo-oval{border-radius:50%;background:radial-gradient(ellipse at 50% 45%,#e9e6e2 0%,#bdb7b1 55%,#55585e 100%);box-shadow:30px 20px 40px rgba(0,0,0,.18)}
.bubble{border-radius:50%;background:#dcdcdc}
/* team */
.team-card{width:274px;height:403px;background:var(--white);box-shadow:0 6px 18px rgba(0,0,0,.25);text-align:center}
.team-photo{width:274px;height:257px;background:linear-gradient(160deg,#9c9a97 0%,#6d6a68 60%,#3e3c3c 100%)}
.team-name{font-size:24px;color:var(--blue);margin-top:12px}
.team-role{font-size:13px;color:var(--text)}
.team-bio{font-size:12px;line-height:18px;color:var(--text);margin:12px 30px 0}
/* contact */
.field{border:2px solid var(--field);border-radius:22px;height:44px;font-size:13px;color:var(--text);padding:0 22px;display:flex;align-items:center}
.field-message{border:2px solid var(--field);border-radius:22px;height:157px;font-size:13px;color:var(--text);padding:18px 22px}
.btn-submit{width:138px;height:36px;border-radius:18px;background:var(--blue);color:var(--white);font-size:12px;font-weight:500;display:flex;align-items:center;justify-content:center}
/* footer */
.footer-contact{left:148px;top:3758px;display:flex;align-items:center;gap:18px;color:var(--white)}
.mail-badge{width:50px;height:50px;border-radius:50%;background:var(--blue);display:flex;align-items:center;justify-content:center}
.footer-contact b{display:block;font-size:16px;font-weight:600}
.footer-contact span{font-size:15px}
.footer-brand{left:510px;top:3743px;width:180px;height:82px;border-radius:50%;background:#e8e8e8;display:flex;align-items:center;justify-content:center;font-size:28px;font-weight:600;color:var(--ink)}
.social{left:904px;top:3763px;display:flex;gap:15px}
.social i{width:40px;height:40px;border-radius:50%;background:var(--blue);display:block}
.footer-rule{left:148px;width:904px;height:1px;background:#262626}
.footer-nav{left:0;top:3882px;width:1200px;display:flex;justify-content:center;gap:70px;font-size:13px;color:var(--white)}
.copyright{left:0;top:3942px;width:1200px;text-align:center;font-size:12px;color:#9a9a9a}
</style>
</head>
<body>

<svg class="backdrop" width="1200" height="3982" viewBox="0 0 1200 3982" aria-hidden="true">
  <polygon points="0,1145 1200,1065 1200,2196 0,2196" fill="var(--grey-band)"/>
  <polygon points="0,1057 380,1122 0,1145" fill="var(--blue)"/>
  <polygon points="0,2196 1200,2170 1200,2690 0,2770" fill="var(--teal-dark)"/>
  <polygon points="680,2760 1200,2690 1200,2868" fill="var(--blue)"/>
  <polygon points="0,3610 490,3690 0,3700" fill="var(--blue)"/>
  <polygon points="0,3700 1200,3655 1200,3982 0,3982" fill="var(--black)"/>
</svg>

<div class="abs top-rule"></div>
<header class="abs site-header">
  <div class="abs brand">Kelvaro <i class="brand-dot"></i></div>
  <nav class="abs main-nav">
    <a class="active">Home</a><a>Vision</a><a>Mission</a><a>Team</a><a>Contact</a>
  </nav>
  <div class="abs phone">
    <svg width="16" height="16" viewBox="0 0 24 24"><path d="M6.6 10.8a15 15 0 0 0 6.6 6.6l2.2-2.2a1 1 0 0 1 1-.25 11 11 0 0 0 3.6.6 1 1 0 0 1 1 1V20a1 1 0 0 1-1 1A17 17 0 0 1 3 4a1 1 0 0 1 1-1h3.5a1 1 0 0 1 1 1 11 11 0 0 0 .6 3.6 1 1 0 0 1-.25 1z" fill="var(--ink)"/></svg>
    +1-555-014-2290
  </div>
</header>

<section class="abs hero" role="img" aria-label="Photo of a smiling woman with glasses working at an office desk"></section>
<h1 class="abs hero-title">WE HELP <b>PEOPLE</b> HELP <b>THEMSELVES</b></h1>
<div class="abs btn-ghost">GET STARTED NOW</div>

<svg class="abs" style="left:580px;top:768px" width="40" height="42" viewBox="0 0 40 42" aria-hidden="true">
  <g fill="none" stroke="#9a9a9a" stroke-width="1.6" stroke-linecap="round">
    <path d="M14 28c0-4-5-6-5-12a11 11 0 0 1 22 0c0 6-5 8-5 12z"/><path d="M15 32h10M16 36h8"/>
    <path d="M20 1v3M4 8l2 2M36 8l-2 2M1 18h3M36 18h3"/>
  </g>
</svg>
<h2 class="abs section-title" style="left:0;top:816px;width:1200px;text-align:center">Welcome to <span>Kelvaro</span></h2>
<p class="abs body-copy" style="left:240px;top:886px;width:720px;text-align:center">We turn research, sharp copy and measured advertising into direct responses that grow real businesses. Every campaign starts with listening, continues with testing and ends with numbers our partners can trust and build on.</p>
<div class="abs btn-more" style="left:531px;top:978px">MORE</div>

<h2 class="abs section-title" style="left:112px;top:1258px">Who <span>We Are ?</span></h2>
<p class="abs body-copy" style="left:112px;top:1312px;width:470px">We are a compact crew of copywriters, researchers and analysts who believe people can lift themselves with the right message. We share what we learn and help our clients grow their own skills along the way.</p>
<div class="abs btn-more" style="left:112px;top:1434px">MORE</div>
<div class="abs photo-oval" style="left:658px;top:1240px;width:430px;height:300px" role="img" aria-label="Photo of two business people shaking hands across a desk"></div>
<div class="abs bubble" style="left:858px;top:1555px;width:52px;height:44px"></div>
<div class="abs bubble" style="left:852px;top:1606px;width:22px;height:18px"></div>

<div class="abs photo-oval" style="left:112px;top:1773px;width:432px;height:224px" role="img" aria-label="Photo of two business people shaking hands across a desk"></div>
<div class="abs bubble" style="left:290px;top:2083px;width:50px;height:42px"></div>
<div class="abs bubble" style="left:322px;top:2132px;width:20px;height:16px"></div>
<h2 class="abs section-title" style="left:624px;top:1812px">What is it <span>that we do ?</span></h2>
<p class="abs body-copy" style="left:624px;top:1868px;width:470px">We write direct response copy, plan advertisements and produce content that moves readers to act. Each piece is researched, tested and refined until it earns attention and delivers results you can clearly measure.</p>
<div class="abs btn-more" style="left:624px;top:1986px">MORE</div>

<h2 class="abs section-title" style="left:0;top:2312px;width:1200px;text-align:center;color:var(--white)">Our Team &amp; Values</h2>
<p class="abs" style="left:190px;top:2372px;width:820px;text-align:center;font-size:13px;line-height:22px;color:#d7e4ec">We’re a small team of smart, funny hard-working specialists who are pushing to become the #1 company in self-reliance. High ambition, radical honesty and a result-oriented mindset are encouraged at Kelvaro.</p>
<article class="abs team-card" style="left:297px;top:2451px">
  <div class="team-photo" role="img" aria-label="Portrait photo of the CEO"></div>
  <h3 class="team-name">Dorin Malec</h3>
  <p class="team-role">CEO Kelvaro</p>
  <p class="team-bio">Dorin started or was involved in 15 failed businesses before discovering online copywriting.</p>
</article>
<article class="abs team-card" style="left:624px;top:2451px">
  <div class="team-photo" role="img" aria-label="Portrait photo of the CEO in a waistcoat"></div>
  <h3 class="team-name">Dorin Malec</h3>
  <p class="team-role">CEO Kelvaro</p>
  <p class="team-bio">Dorin started or was involved in 15 failed businesses before discovering online copywriting.</p>
</article>
<div class="abs btn-more" style="left:531px;top:2916px">MORE</div>

<h2 class="abs section-title" style="left:0;top:3032px;width:1200px;text-align:center">Contact <span>Us</span></h2>
<div class="abs field" style="left:244px;top:3122px;width:343px">Full Name</div>
<div class="abs field" style="left:605px;top:3122px;width:343px">Email</div>
<div class="abs field" style="left:244px;top:3183px;width:704px">Website</div>
<div class="abs field" style="left:244px;top:3246px;width:704px">Website</div>
<div class="abs field-message" style="left:244px;top:3308px;width:704px">Message</div>
<div class="abs btn-submit" style="left:244px;top:3500px">SUBMIT</div>

<div class="abs footer-contact">
  <div class="mail-badge"><svg width="24" height="18" viewBox="0 0 24 18"><rect x="1" y="1" width="22" height="16" rx="2" fill="none" stroke="#fff" stroke-width="2"/><path d="M1 2l11 8 11-8" fill="none" stroke="#fff" stroke-width="2"/></svg></div>
  <div><b>EMAIL:</b><span>hello@kelvaro.example</span></div>
</div>
<div class="abs footer-brand">Kelvaro</div>
<div class="abs social" aria-label="Social links"><i></i><i></i><i></i></div>
<div class="abs footer-rule" style="top:3858px"></div>
<nav class="abs footer-nav"><span>Home</span><span>Vision</span><span>Mission</span><span>Team</span><span>Contact</span></nav>
<div class="abs footer-rule" style="top:3920px"></div>
<p class="abs copyright">copyright © 2018 KELVARO. All Rights Reserved</p>

</body>
</html>
```